Flyer design for mobile apps service for small/medium businesses

KelvoraPocket is a service line of KelvoraWorks Ltd, which aims to provide a bespoke mobile app building service to small and medium businesses. The focus of this business is to team closely with the small business to understand their motivation and advise them on gaining a mobile presence, first a small one, then to grow as their customers feed back their approval.I would like mainly use of the colours in the app logo (green and gold) but others could be use for emphasizing text.The final design should communicate "we are on the side of small business, want you to succeed in getting a mobile presence"The reverse side of the flyer should say something about the company and its approach to doing this, as well as include contact info and a QR code of the website (kelvorapocket.uk)The images I am providing include six of typical small businesses, one of arms holding mobile phones, one of mobile devices exploding with apps. ALso the logo for kelvorapocket, which should be prominent..

Target Market(s)

Small business owners

Industry/Entity Type

Building

Requirements
Must have
• Images of small businesses (provided)
• Logo
• Key text entries (all or some of - see attached word doc)
• The strapline for the business: "The Smarter Business Gets Mobile"
• Consistent colour scheme
• Reverse side with contact info and QR code of websirte

```html
<!DOCTYPE html>
<html lang="en">
<head>
<meta charset="utf-8">
<title>KelvoraPocket Flyers</title>
<link href="https://fonts.googleapis.com/css2?family=Open+Sans:wght@400;600;700;800&family=Roboto+Condensed:wght@700&display=swap" rel="stylesheet">
<style>
:root{
  --green:#1f6b35;
  --green-bright:#1d8a45;
  --green-dark:#17331f;
  --gold:#f2d338;
  --gold-deep:#e8c21e;
  --ink:#1c1c1c;
  --white:#ffffff;
  --stage:#e4e4e4;
}
*{margin:0;padding:0;box-sizing:border-box}
html,body{width:1200px;height:1200px;overflow:hidden;background:var(--stage)}
body{position:relative;font-family:"Open Sans",Arial,sans-serif;color:var(--ink)}
.flyer{position:absolute;width:574px;height:810px;background:var(--white);overflow:hidden;box-shadow:0 4px 14px rgba(0,0,0,.25)}
.flyer--front{left:21px;top:124px}
.flyer--back{left:609px;top:297px}
.abs{position:absolute}
.cond{font-family:"Roboto Condensed","Arial Narrow",sans-serif;font-weight:700}

/* front */
.collage{left:0;top:0;width:574px;height:345px;display:grid;grid-template-columns:230px 190px 154px;grid-template-rows:165px 180px}
.collage .ph{width:100%;height:100%}
.ph-a{background:linear-gradient(135deg,#3a4658,#8a95a3)}
.ph-b{background:linear-gradient(135deg,#c79a73,#e8c7c0)}
.ph-c{background:linear-gradient(135deg,#3c4f72,#cfd4da)}
.ph-d{background:linear-gradient(135deg,#2a2a2a,#9b8a80)}
.ph-e{background:linear-gradient(135deg,#dfe6ec,#f2d2c4)}
.ph-f{background:linear-gradient(135deg,#5a6a55,#c9c7a8)}
.swoosh{left:0;top:280px;width:574px;height:100px}
.boy{left:0;top:300px;width:200px;height:360px;background:linear-gradient(160deg,#e9e3dc 0%,#d8a98c 35%,#c8443c 75%,#b73530 100%)}
.logo-box{left:155px;top:130px;width:286px;height:80px;background:var(--white);display:flex;align-items:center;justify-content:center;gap:10px}
.logo-dot{width:26px;height:26px;border-radius:50%;background:var(--green-bright)}
.logo-name{font-family:"Open Sans",Arial,sans-serif;font-weight:700;color:var(--gold-deep);font-size:34px;letter-spacing:-.5px}
.band{left:187px;top:344px;width:387px;height:178px;background:var(--green);color:var(--white);text-align:center;padding-top:16px}
.strap{font-size:21px;font-weight:400;letter-spacing:.2px}
.boost{font-size:34px;color:var(--gold);line-height:1;margin-top:10px}
.ownapp{font-size:27px;line-height:1;margin-top:2px}
.help{font-size:15px;line-height:1.3;margin-top:12px}
.intro{left:212px;top:540px;width:340px;font-size:12.8px;line-height:1.38;letter-spacing:-.1px}
.cta-left{left:0;top:660px;width:311px;height:92px;background:linear-gradient(90deg,#f6e47a,var(--gold));text-align:center;padding-top:12px}
.cta-title{font-family:"Open Sans",Arial,sans-serif;font-weight:800;color:var(--green);font-size:24px;line-height:1}
.cta-sub{font-size:13.5px;line-height:1.4;margin-top:5px}
.hands{left:311px;top:660px;width:263px;height:92px;background:linear-gradient(135deg,#eef0f0,#cfd6d6)}
.foot{left:0;top:752px;width:574px;height:58px;background:var(--green);color:var(--white);display:flex;align-items:center;justify-content:space-around;font-size:21px}

/* back */
.hl{left:0;width:574px;text-align:center;line-height:1;white-space:nowrap}
.h-does{top:10px;font-size:72px;font-weight:400;color:var(--green-dark);letter-spacing:4px}
.h-business{top:80px;font-size:44px;font-weight:800;color:var(--green-dark);letter-spacing:1px}
.h-mobile{top:112px;height:109px;font-size:109px;font-weight:400;color:var(--gold);display:flex;justify-content:center;align-items:center;letter-spacing:3px}
.globe{display:inline-block;width:86px;height:86px;border-radius:50%;background:radial-gradient(circle at 40% 40%,#e8f0fa,#6f9fd6 70%,#3d6fb0);margin:6px 8px 0 6px}
.h-presence{top:205px;font-size:77px;font-weight:400;color:var(--green-bright);letter-spacing:5px}
.usage{left:0;top:293px;width:261px;height:146px;background:var(--green);color:var(--white);padding:12px 0 0 41px;font-size:19px;line-height:1.36}
.usage b{color:var(--gold);font-weight:700}
.doodle{left:267px;top:307px;width:288px;height:190px;background:linear-gradient(135deg,#ffffff,#e6ebe8)}
.logo-back{left:38px;top:451px;height:52px;display:flex;align-items:center;gap:8px}
.logo-back .logo-name{font-size:30px}
.logo-back .logo-dot{width:22px;height:22px}
.body-copy{left:35px;top:519px;width:262px;font-size:13.5px;line-height:16px;letter-spacing:-.2px}
.body-copy p+p{margin-top:16px}
.cta-right{left:311px;top:507px;width:263px;height:244px;background:var(--gold);text-align:center;padding-top:24px}
.dont{font-size:19px;line-height:1}
.join{font-size:33px;font-weight:800;line-height:1;margin-top:10px}
.world{font-size:19px;font-weight:800;line-height:1}
.cta-right .cta-title{font-size:26px;margin-top:14px}
.cta-right .cta-sub{font-size:13.8px;margin-top:3px;line-height:1.4}
.foot-back{left:0;top:751px;width:574px;height:59px;background:var(--green);color:var(--white);display:flex;align-items:center;font-size:21px}
.foot-back .phone{width:315px;text-align:center;border-right:1px solid rgba(255,255,255,.7);height:38px;line-height:38px}
.foot-back .web{flex:1;text-align:center}
</style>
</head>
<body>

<section class="flyer flyer--front">
  <div class="abs collage">
    <div class="ph ph-a" role="img" aria-label="Photo of mechanics fitting a car windscreen"></div>
    <div class="ph ph-b" role="img" aria-label="Photo of a florist in her shop"></div>
    <div class="ph ph-c" role="img" aria-label="Photo of two tradesmen with tool belts"></div>
    <div class="ph ph-d" role="img" aria-label="Photo of hairdressers at work"></div>
    <div class="ph ph-e" role="img" aria-label="Photo of a dentist treating a patient"></div>
    <div class="ph ph-f" role="img" aria-label="Photo of a bicycle repair worker"></div>
  </div>
  <svg class="abs swoosh" viewBox="0 0 574 100" preserveAspectRatio="none" aria-hidden="true">
    <path d="M0 20 Q300 40 574 65 L574 100 L0 100Z" fill="#fff"/>
    <path d="M0 16 Q300 38 574 60 L574 68 Q300 44 0 24Z" fill="#f2d338"/>
  </svg>
  <div class="abs boy" role="img" aria-label="Photo of a smiling young man using a smartphone"></div>
  <div class="abs logo-box"><span class="logo-dot"></span><span class="logo-name">KelvoraPocket</span></div>
  <div class="abs band">
    <p class="strap">The Smarter Business Gets Mobile</p>
    <p class="boost cond">BOOST YOUR BUSINESS</p>
    <p class="ownapp cond">WITH YOUR OWN MOBILE APP</p>
    <p class="help">WE CAN HELP YOU BUILD<br>A MOBILE PRESENCE FOR YOUR BUSINESS</p>
  </div>
  <p class="abs intro">We are a small business ourselves, based here in the UK (Kent), and our mission is to support other local businesses by helping them take advantage of the mobile world. Whatever business you run, however small, it is in your interest to explore the benefits of the mobile world, so please get in touch!</p>
  <div class="abs cta-left">
    <p class="cta-title">CONTACT US NOW</p>
    <p class="cta-sub">to discuss the possibilities for a<br>business like yours</p>
  </div>
  <div class="abs hands" role="img" aria-label="Illustration of hands holding up smartphones"></div>
  <div class="abs foot cond"><span>020-84915307, 07700-900482</span><span>www.kelvorapocket.uk</span></div>
</section>

<section class="flyer flyer--back">
  <p class="abs hl h-does">DOES YOUR</p>
  <p class="abs hl h-business">BUSINESS HAVE A</p>
  <p class="abs hl h-mobile">M<span class="globe" role="img" aria-label="Globe illustration forming the letter O"></span>BILE</p>
  <p class="abs hl h-presence">PRESENCE?</p>
  <div class="abs usage">
    Almost everyone<br>is using Mobile Devices<br>these days<br>
    <b>Shouldn't your<br>business be on them?</b>
  </div>
  <div class="abs doodle" role="img" aria-label="Sketch of a cartoon figure holding hands with a smartphone"></div>
  <div class="abs logo-back"><span class="logo-dot"></span><span class="logo-name">KelvoraPocket</span></div>
  <div class="abs body-copy">
    <p>This is a great opportunity to put your business on those all-pervasive devices that people never seem to put down!</p>
    <p>With a mobile app for your business you can make it easier for customers to book appointments, access discounts, view your products/services and communicate with you</p>
    <p>It may be cheaper than you think to produce a mobile app that allows your customers to engage with you like they never could before!</p>
  </div>
  <div class="abs cta-right">
    <p class="dont">Don't disadvantage<br>your business</p>
    <p class="join">JOIN THE</p>
    <p class="world">MOBILE WORLD</p>
    <p class="cta-title">CONTACT US NOW</p>
    <p class="cta-sub">to discuss the possibilities for a<br>business like yours<br>(you may be surprised!)</p>
  </div>
  <div class="abs foot-back cond"><span class="phone">020-84915307, 07700-900482</span><span class="web">www.kelvorapocket.uk</span></div>
</section>

</body>
</html>
```